Visitenkarten für Containerhandel
BROV
alles tip top wie bestellt so wurde geliefert!
Zielgruppe
Wir handeln mit See und Lagercontainer
Aufgabenstellung
evtl. Das Seecontainer Designe integrieren
Angaben auf der Karte;
//Frimenangaben//
TORVELMARK AG
Ribelweg 27
CH - 5712 Stelden
sales@torvelmark.ch
//Personenangaben//
Lukas Brenni
Leiter Verkauf

```html
<!DOCTYPE html>
<html lang="de">
<head>
<meta charset="utf-8">
<title>TORVELMARK AG – Visitenkarten</title>
<link href="https://fonts.googleapis.com/css2?family=Arimo:wght@400;700&display=swap" rel="stylesheet">
<style>
  :root {
    --navy: #123a6e;
    --blue: #1f8ad8;
    --sky: #a9d6f1;
    --ink: #222326;
    --grey: #b9bcc0;
    --paper: #ffffff;
    --backdrop: #e9e6e2;
  }
  * { margin: 0; padding: 0; box-sizing: border-box; }
  html, body { width: 1200px; height: 900px; overflow: hidden; }
  body {
    background: var(--backdrop);
    font-family: "Arimo", Arial, sans-serif;
    display: flex;
    flex-direction: column;
    align-items: center;
    justify-content: center;
    gap: 56px;
  }
  .card {
    position: relative;
    width: 560px;
    height: 362px;
    background: var(--paper);
    box-shadow: 0 10px 28px rgba(0,0,0,.14);
    overflow: hidden;
  }
  .card-shapes { position: absolute; inset: 0; width: 100%; height: 100%; }

  /* Vorderseite */
  .brand-corner {
    position: absolute; top: 38px; right: 44px;
    font-weight: 700; font-size: 30px; letter-spacing: 1px;
    color: var(--grey); line-height: 1;
  }
  .person { position: absolute; top: 52px; left: 40px; }
  .person-name {
    font-weight: 700; font-size: 22px; color: var(--ink);
    text-transform: uppercase; letter-spacing: .3px;
  }
  .person-role { font-size: 19px; color: var(--blue); margin-top: 2px; }

  .contact-row {
    position: absolute; left: 40px;
    display: flex; align-items: center; gap: 12px;
    color: var(--paper); font-size: 15px; line-height: 1.2;
  }
  .contact-row svg { flex: none; width: 26px; height: 26px; }
  .contact-phone { top: 118px; }
  .contact-address { top: 180px; }
  .contact-mail { top: 262px; }
  .company { font-weight: 700; text-transform: uppercase; }

  /* Rückseite */
  .brand-center {
    position: absolute; top: 50%; left: 50%;
    transform: translate(-50%, -60%);
    display: flex; align-items: center; gap: 14px;
  }
  .brand-mark { width: 22px; height: 22px; background: var(--ink); }
  .brand-name {
    font-weight: 700; font-size: 56px; color: var(--ink);
    letter-spacing: 1px; line-height: 1;
  }
</style>
</head>
<body>

  <section class="card card-front" aria-label="Visitenkarte Vorderseite">
    <svg class="card-shapes" viewBox="0 0 560 362" aria-hidden="true">
      <polygon points="330,0 560,0 560,8 325,20" fill="var(--navy)"/>
      <polygon points="350,20 560,8 560,14 348,24" fill="var(--blue)"/>
      <polygon points="0,112 290,112 330,150 0,150" fill="var(--navy)"/>
      <polygon points="0,150 330,150 420,130 560,130 560,150 360,330 0,330" fill="var(--blue)"/>
      <polygon points="420,130 560,130 560,150 470,240" fill="var(--sky)"/>
    </svg>

    <div class="brand-corner">TORVELMARK</div>

    <div class="person">
      <div class="person-name">Lukas Brenni</div>
      <div class="person-role">Leiter Verkauf</div>
    </div>

    <div class="contact-row contact-phone">
      <svg viewBox="0 0 28 28"><circle cx="14" cy="14" r="13" fill="var(--paper)"/><rect x="10" y="7" width="8" height="14" rx="1.5" fill="none" stroke="var(--navy)" stroke-width="1.6"/><circle cx="14" cy="18.5" r=".9" fill="var(--navy)"/></svg>
      <span>+41 58 730 42 16</span>
    </div>

    <div class="contact-row contact-address">
      <svg viewBox="0 0 28 28"><circle cx="14" cy="14" r="13" fill="var(--paper)"/><path d="M14 6a5 5 0 0 1 5 5c0 4-5 10-5 10s-5-6-5-10a5 5 0 0 1 5-5z" fill="var(--blue)"/><circle cx="14" cy="11" r="1.8" fill="var(--paper)"/></svg>
      <span><span class="company">TORVELMARK AG</span><br>Ribelweg 27<br>CH - 5712 Stelden</span>
    </div>

    <div class="contact-row contact-mail">
      <svg viewBox="0 0 28 28"><circle cx="14" cy="14" r="13" fill="var(--paper)"/><rect x="7.5" y="9.5" width="13" height="9" fill="none" stroke="var(--blue)" stroke-width="1.6"/><path d="M7.5 9.5l6.5 5 6.5-5" fill="none" stroke="var(--blue)" stroke-width="1.6"/></svg>
      <span>sales@torvelmark.ch</span>
    </div>
  </section>

  <section class="card card-back" aria-label="Visitenkarte Rückseite">
    <svg class="card-shapes" viewBox="0 0 560 362" aria-hidden="true">
      <polygon points="0,330 260,300 262,307 0,338" fill="var(--navy)"/>
      <polygon points="270,298 560,265 560,274 268,306" fill="var(--blue)"/>
    </svg>
    <div class="brand-center">
      <span class="brand-mark"></span>
      <span class="brand-name">TORVELMARK</span>
    </div>
  </section>

</body>
</html>
```